High-end residential home builder needs a business card design

We need a new business card design for a small residential construction company based in Boise, Idaho. We specialize in building custom high-end homes and remodels, with a focus on great design and craftsmanship.

We would like to use our current logo, but open to new color suggestions.
Just looking for a clean, sharp, modern design that looks high-end.

Target Market(s)

Upscale clientele

Industry/Entity Type

Contractor

Contact Information for Business Card

Company: Stonefield Custom Builders
Name: Marcus Tilley
Phone number: 208 367 4120
Email: MarcusTilleySCB@mailbox-example.com
Website: Stonefieldcustombuilders-example.com

Font styles to use
Serif
Sans Serif

Requirements
Must have
• Company Logo
Company name
My name
My phone number
My email
Company website
Nice to have
• I have attached a few photos of cards that I really like.

```html
<!DOCTYPE html>
<html lang="en">
<head>
<meta charset="utf-8">
<title>Stonefield Custom Builders – Business Card</title>
<link href="https://fonts.googleapis.com/css2?family=Raleway:wght@300;400;600;700&display=swap" rel="stylesheet">
<style>
  :root {
    --stage: #151515;
    --paper: #f9fafb;
    --brand-orange: #dc8b2c;
    --brand-orange-light: #e4922f;
    --brand-brown: #2b1a10;
    --white: #ffffff;
  }
  * { margin: 0; padding: 0; box-sizing: border-box; }
  html, body {
    width: 1006px; height: 1200px; overflow: hidden;
    background: var(--stage);
    font-family: "Raleway", Arial, sans-serif;
  }
  .card {
    position: absolute; left: 81px; width: 845px; height: 483px;
    overflow: hidden; text-align: center;
  }
  .card--front { top: 79px; background: var(--paper); }
  .card--back { top: 638px; background: var(--brand-orange); }

  .photo-wash { position: absolute; inset: 0; }
  .card--front .photo-wash {
    background: radial-gradient(ellipse at 50% 65%, rgba(225,228,232,0.55), rgba(249,250,251,0) 70%);
  }
  .card--back .photo-wash {
    background: linear-gradient(180deg, rgba(219,139,44,0) 0%, rgba(232,150,50,0.6) 55%, rgba(214,132,38,0.5) 100%);
  }
  .corner-accent { position: absolute; }
  .corner-accent--top { left: 0; top: 0; width: 108px; height: 108px; }
  .corner-accent--bottom { right: 0; bottom: 0; width: 195px; height: 195px; }
  .card--front .corner-accent--top { background: radial-gradient(circle at 0 0, rgba(220,222,226,0.7), rgba(249,250,251,0) 70%); }
  .card--front .corner-accent--bottom { background: radial-gradient(circle at 100% 100%, rgba(220,222,226,0.8), rgba(249,250,251,0) 70%); }
  .card--back .corner-accent--top { background: radial-gradient(circle at 0 0, rgba(255,255,255,0.25), rgba(255,255,255,0) 70%); }
  .card--back .corner-accent--bottom { background: radial-gradient(circle at 100% 100%, rgba(255,255,255,0.25), rgba(255,255,255,0) 70%); }

  .brand-mark {
    position: absolute; left: 50%; transform: translateX(-50%);
    border: 3px solid currentColor;
  }
  .card--front .brand-mark { top: 140px; width: 68px; height: 68px; color: var(--brand-brown); }
  .card--back .brand-mark { top: 178px; width: 46px; height: 46px; color: var(--white); border-width: 2px; }

  .brand-name {
    position: absolute; left: 0; right: 0;
    font-weight: 700; text-transform: uppercase;
  }
  .card--front .brand-name {
    top: 300px; font-size: 22px; letter-spacing: 6px; color: var(--brand-brown);
  }
  .card--back .brand-name {
    top: 236px; font-size: 11px; letter-spacing: 4px; color: var(--white); font-weight: 600;
  }

  .website {
    position: absolute; left: 0; right: 0; top: 430px;
    font-size: 19px; font-weight: 400; letter-spacing: 1px; color: var(--brand-orange);
  }

  .person-name {
    position: absolute; left: 0; right: 0; top: 92px;
    font-size: 34px; font-weight: 700; letter-spacing: 12px; color: var(--white);
    padding-left: 12px;
  }
  .person-title {
    position: absolute; left: 0; right: 0; top: 292px;
    font-size: 21px; font-weight: 600; letter-spacing: 6px; color: var(--white);
  }
  .contact {
    position: absolute; left: 0; right: 0; top: 348px;
    list-style: none; color: var(--white);
    font-size: 16px; font-weight: 400; letter-spacing: 3px; line-height: 26.5px;
  }
</style>
</head>
<body>
  <section class="card card--front">
    <div class="photo-wash" role="img" aria-label="Faint photograph of a modern custom home"></div>
    <div class="corner-accent corner-accent--top" role="img" aria-label="Faint geometric corner accent"></div>
    <div class="corner-accent corner-accent--bottom" role="img" aria-label="Faint geometric corner accent"></div>
    <div class="brand-mark"></div>
    <p class="brand-name">Stonefield Custom Builders</p>
    <p class="website">www.stonefieldcustombuilders-example.com</p>
  </section>

  <section class="card card--back">
    <div class="photo-wash" role="img" aria-label="Faint photograph of a modern custom home tinted orange"></div>
    <div class="corner-accent corner-accent--top" role="img" aria-label="Faint geometric corner accent"></div>
    <div class="corner-accent corner-accent--bottom" role="img" aria-label="Faint geometric corner accent"></div>
    <h1 class="person-name">MARCUS TILLEY</h1>
    <div class="brand-mark"></div>
    <p class="brand-name">Stonefield Custom Builders</p>
    <p class="person-title">OWNER &amp; FOUNDER</p>
    <ul class="contact">
      <li>stonefieldcustombuilders-example.com</li>
      <li>marcustilleyscb@mailbox-example.com</li>
      <li>208-367-4120</li>
    </ul>
  </section>
</body>
</html>
```